Corvell Tiling Solutions, QBCC 8471302, ABN 48290517736, Email corvelltiling@brindlemail.com,Mobile 04958142

Corvell Tiling Solutions, is the name of my wall and floor tiling company and the details above are needed on the business card. Im open to see what people come up with i really have no colour requirements or other design specs as long as its not too plain.

```html
<!DOCTYPE html>
<html lang="en">
<head>
<meta charset="utf-8">
<title>Corvell Tiling Solutions – Business Card</title>
<link rel="stylesheet" href="https://fonts.googleapis.com/css2?family=Rokkitt:wght@400;500;700&display=swap">
<style>
  :root {
    --card-bg: #ffffff;
    --ink: #111111;
    --tile: #bcbcbd;
    --frame: #222222;
  }
  html, body {
    margin: 0;
    padding: 0;
    overflow: hidden;
    background: var(--card-bg);
  }
  .card {
    position: relative;
    width: 1200px;
    height: 723px;
    background: var(--card-bg);
    box-sizing: border-box;
    border: 2px solid var(--frame);
    overflow: hidden;
    font-family: "Rokkitt", serif;
    color: var(--ink);
  }
  .tiles {
    position: absolute;
    inset: 0;
  }
  .tile { fill: var(--tile); }
  .condensed {
    transform: scaleX(0.84);
    transform-origin: left top;
    white-space: nowrap;
  }
  .company-name {
    position: absolute;
    left: 78px;
    top: 32px;
    margin: 0;
    font-weight: 700;
    font-size: 110px;
    line-height: 153px;
  }
  .contact-person {
    position: absolute;
    left: 682px;
    top: 274px;
    margin: 0;
  }
  .person-name {
    display: block;
    font-weight: 500;
    font-size: 54px;
    line-height: 60px;
  }
  .person-role {
    display: block;
    margin-left: 36px;
    font-weight: 500;
    font-size: 30px;
    line-height: 40px;
  }
  .contact-details {
    position: absolute;
    left: 764px;
    top: 450px;
    margin: 0;
    font-style: normal;
    font-weight: 500;
    font-size: 33px;
    line-height: 55.5px;
  }
</style>
</head>
<body>
<div class="card">
  <svg class="tiles" width="1200" height="723" viewBox="0 0 1200 723" aria-hidden="true">
    <rect class="tile" x="834" y="42" width="153" height="153"/>
    <rect class="tile" x="1005" y="42" width="153" height="153"/>
    <rect class="tile" x="1005" y="211" width="153" height="153"/>
    <rect class="tile" x="216" y="355" width="153" height="153"/>
    <rect class="tile" x="385" y="355" width="153" height="153"/>
    <rect class="tile" x="47" y="524" width="153" height="153"/>
    <rect class="tile" x="216" y="524" width="153" height="153"/>
    <rect class="tile" x="554" y="524" width="153" height="153"/>
  </svg>

  <h1 class="company-name condensed">Corvell Tiling<br>Solutions</h1>

  <p class="contact-person condensed">
    <span class="person-name">Mrs. Harlow</span>
    <span class="person-role">consultant</span>
  </p>

  <address class="contact-details condensed">
    QBCC 8471302<br>
    ABN 48290517736<br>
    mobile 04958142<br>
    corvelltiling@brindlemail.com
  </address>
</div>
</body>
</html>
```